Business Card Design

I need a new business card design for myself. I am a life coach and therapist with both a private practice and now a newly formed business see both my websites: I am looking for a business card to support this and be close to the colours and design of my private practice website and my business website. I am looking for strong bright nature based colours. Sun, Sea and Greenery. The card should reflect inspiration, enlightenment, empowerment and strength!!!
www.helenaroseharwick.com and
www.clear-paths-mentoring.co.uk
Updates
Thank you everyone for your designs. I will be making a final decision by the end of this week and will notify you as soon as possible after this.
Industry/Entity Type
Business
Contact Information for Business Card
Helena Rose Harwick, BSc, PGDip & MRes
Therapist and Life Coach
Clear Paths Mentoring
17 Wexley Road
Manchester
M4 7QT
0800 0619482 Mobile: 07738264917
email: hrharwick@helenaroseharwick.com
Requirements
Must have
- not too busy. To be clear and easy to read information..
and to include this tag line:
"helping you live your life with passion and confidence"

```html
<!DOCTYPE html>
<html lang="en">
<head>
<meta charset="utf-8">
<title>Helena Rose Harwick – Business Card</title>
<link href="https://fonts.googleapis.com/css2?family=PT+Sans:wght@400&display=swap" rel="stylesheet">
<style>
  :root {
    --backdrop: #1f2224;
    --lime: #99ff00;
    --lime-glow: #dcffb0;
    --lime-mid: #b8ff4a;
    --forest-dark: #0f2a12;
    --forest: #2f6b2a;
    --forest-light: #5f9a3a;
    --ink: #ffffff;
  }
  * { margin: 0; padding: 0; box-sizing: border-box; }
  html, body {
    width: 1200px;
    height: 733px;
    overflow: hidden;
    background: var(--backdrop);
    font-family: "PT Sans", sans-serif;
  }
  .stage {
    width: 1200px;
    height: 733px;
    display: flex;
    align-items: center;
    justify-content: center;
    gap: 50px;
  }
  .card {
    position: relative;
    width: 540px;
    height: 348px;
    overflow: hidden;
    color: var(--ink);
    text-shadow: 0 0 6px rgba(255, 255, 255, 0.45), 0 1px 2px rgba(60, 110, 0, 0.35);
  }
  .card--front {
    background: radial-gradient(ellipse 55% 60% at 50% 62%, var(--lime-glow) 0%, var(--lime-mid) 45%, var(--lime) 100%);
    display: flex;
    flex-direction: column;
    align-items: center;
    justify-content: center;
    padding-top: 34px;
    text-align: center;
  }
  .front__name {
    font-size: 35px;
    letter-spacing: 0.5px;
    line-height: 1.15;
  }
  .front__role,
  .front__company {
    font-size: 24px;
    line-height: 1.3;
  }
  .card--back {
    background: radial-gradient(ellipse 60% 55% at 40% 45%, var(--lime-glow) 0%, var(--lime-mid) 40%, var(--lime) 100%);
  }
  .back__photo {
    position: absolute;
    inset: 0;
    width: 540px;
    height: 348px;
  }
  .back__details {
    position: absolute;
    left: 42px;
    top: 170px;
    font-size: 18px;
    line-height: 1.3;
  }
  .back__address { margin-bottom: 24px; }
  .back__tagline {
    position: absolute;
    left: 42px;
    bottom: 26px;
    font-size: 15px;
  }
</style>
</head>
<body>
<main class="stage">
  <section class="card card--back" aria-label="Card back">
    <svg class="back__photo" viewBox="0 0 540 348" aria-hidden="false">
      <defs>
        <linearGradient id="forestTone" x1="0" y1="0" x2="1" y2="1">
          <stop offset="0" stop-color="var(--forest-dark)"/>
          <stop offset="0.5" stop-color="var(--forest)"/>
          <stop offset="1" stop-color="var(--forest-light)"/>
        </linearGradient>
      </defs>
      <polygon role="img" aria-label="Photograph of a waterfall in lush green rainforest"
               points="215,0 540,0 540,170 300,170" fill="url(#forestTone)"/>
    </svg>
    <div class="back__details">
      <p class="back__address">17 Wexley Road<br>Manchester M4 7QT 0800 0619482</p>
      <p class="back__contact">Mobile: 07738264917<br>email: hrharwick@helenaroseharwick.com</p>
    </div>
    <p class="back__tagline">"helping you live your life with passion and confidence"</p>
  </section>

  <section class="card card--front" aria-label="Card front">
    <h1 class="front__name" style="font-weight:400">Helena Rose Harwick</h1>
    <p class="front__role">Executive Life Coach</p>
    <p class="front__company">Clear Paths Mentoring</p>
  </section>
</main>
</body>
</html>
```